Harriet Voss Consortium - Paediatric Lower Limb Surgery Agenda Forming Collective

A 2-sided A4 leaflet to explain the research priorities in Children's Orthopaedic Surgery.
We would like this to be similar to that produced previously by the physiotherapists.

```html
<!DOCTYPE html>
<html lang="en">
<head>
<meta charset="utf-8">
<title>Harriet Voss Consortium – Research Priorities Leaflet</title>
<link rel="stylesheet" href="https://fonts.googleapis.com/css2?family=Libre+Baskerville:wght@700&family=Oswald:wght@500;600&family=Questrial&display=swap">
<style>
:root{
  --stage:#ececec;
  --paper:#ffffff;
  --navy:#3c3a8f;
  --red:#d7222c;
  --ink:#3a3a3a;
  --num:#1f5357;
  --card-a:#f6f6f6;
  --card-b:#e4e4e4;
  --yellow:#f5d51e;
  --amber:#f3aa1c;
  --lime:#e2e33a;
  --lime-d:#d3d325;
  --sage:#a9cdbf;
  --sage-d:#79b1a0;
  --teal:#1c9ca8;
  --teal-d:#117c86;
  --orange:#f5a623;
  --orange-d:#f18a14;
}
*{box-sizing:border-box;margin:0;padding:0}
html,body{width:720px;height:1200px;overflow:hidden}
body{background:var(--stage);position:relative;font-family:"Questrial",sans-serif;color:var(--ink)}
.page{position:absolute;left:174px;width:372px;background:var(--paper);overflow:hidden;box-shadow:0 2px 8px rgba(0,0,0,.12)}
.page--front{top:50px;height:528px}
.page--back{top:626px;height:524px}

/* front */
.title{position:absolute;right:20px;top:22px;text-align:right;font-family:"Libre Baskerville",serif;font-weight:700;line-height:1.22;font-size:15.5px}
.title .line{display:block}
.title .blue{color:var(--navy)}
.title .red{color:var(--red)}
.wheel{position:absolute;left:0;top:0}
.seg-text{position:absolute;color:#fff;font-size:5.2px;line-height:1.32}
.seg-text h2{font-family:"Oswald",sans-serif;font-weight:500;font-size:15px;line-height:1;margin-bottom:4px;letter-spacing:.2px}
.seg-text--ask{left:22px;top:126px;width:72px}
.seg-text--analyse{left:136px;top:294px;width:70px}
.seg-text--prioritise{left:20px;top:408px;width:118px}
.hub-name{position:absolute;left:16px;top:282px;width:84px;text-align:center;color:var(--red);font-size:7px;line-height:1.25}
.hub-mark{display:block;width:12px;height:12px;background:var(--navy);margin:0 auto 4px}
.intro{position:absolute;right:20px;top:150px;width:122px;text-align:right;font-size:9.3px;line-height:1.2;color:#333}
.intro p+p{margin-top:10px}
.front-partners{position:absolute;left:160px;right:18px;top:474px;display:flex;justify-content:space-between;align-items:center}
.partner{display:flex;align-items:center;gap:4px;font-size:7.4px;line-height:1.15}
.partner--voss{color:var(--navy);width:82px}
.partner--kestrel{color:var(--red);width:98px}
.partner .dot{flex:0 0 10px;height:10px;border-radius:50%;background:currentColor}
.partner .sq{flex:0 0 10px;height:10px;background:currentColor}

/* back */
.back-title{position:absolute;top:22px;left:0;right:0;text-align:center;font-family:"Oswald",sans-serif;font-weight:500;font-size:15px;color:var(--navy);letter-spacing:-.1px}
.priority{position:absolute;height:60px}
.priority--left{left:20px;width:170px}
.priority--right{left:194px;width:166px}
.priority .card{position:absolute;top:3px;height:54px;width:140px;border-radius:6px;background:linear-gradient(180deg,var(--card-a),var(--card-b));box-shadow:0 2px 4px rgba(0,0,0,.12);display:flex;align-items:center;font-size:5.1px;line-height:1.3;text-align:justify;color:#444}
.priority--left .card{left:28px;padding:0 6px 0 34px}
.priority--right .card{left:0;padding:0 38px 0 8px}
.badge{position:absolute;top:2px;width:56px;height:56px;border-radius:50%;display:flex;align-items:center;justify-content:center;box-shadow:0 2px 4px rgba(0,0,0,.15)}
.priority--left .badge{left:0}
.priority--right .badge{left:110px}
.badge span{width:38px;height:38px;border-radius:50%;display:flex;align-items:center;justify-content:center;font-family:"Oswald",sans-serif;font-weight:600;font-size:20px;color:var(--num);box-shadow:inset 0 0 0 2px rgba(255,255,255,.35)}
.b-yellow{background:var(--yellow)} .b-yellow span{background:var(--amber)}
.b-lime{background:var(--lime)} .b-lime span{background:var(--lime-d)}
.b-sage{background:var(--sage)} .b-sage span{background:var(--sage-d)}
.b-teal{background:var(--teal)} .b-teal span{background:var(--teal-d)}
.b-orange{background:var(--orange)} .b-orange span{background:var(--orange-d)}
.b-lemon{background:var(--lime)} .b-lemon span{background:var(--yellow)}
.thanks{position:absolute;left:20px;top:436px;width:170px;font-size:7.6px;line-height:1.2;color:#222}
.credits{position:absolute;left:20px;right:20px;top:476px;display:flex;align-items:center;justify-content:space-between}
.credits h3{font-family:"Questrial",sans-serif;font-size:6px;font-weight:400;letter-spacing:.3px;color:#222}
.credits .partner{font-size:6px;width:auto;max-width:80px}
.partner--guild{color:var(--navy)}
</style>
</head>
<body>

<section class="page page--front">
  <svg class="wheel" width="372" height="528" viewBox="0 0 372 528">
    <defs>
      <linearGradient id="g-ask" x1="0" y1="0" x2="1" y2="1"><stop offset="0" stop-color="#17a9e6"/><stop offset="1" stop-color="#20cdb0"/></linearGradient>
      <linearGradient id="g-analyse" x1="0" y1="0" x2="1" y2="1"><stop offset="0" stop-color="#d3168a"/><stop offset="1" stop-color="#5d2c9c"/></linearGradient>
      <linearGradient id="g-prior" x1="0" y1="1" x2="1" y2="0"><stop offset="0" stop-color="#e8157f"/><stop offset="1" stop-color="#f4742a"/></linearGradient>
      <filter id="soft" x="-20%" y="-20%" width="140%" height="140%"><feDropShadow dx="0" dy="2" stdDeviation="3" flood-opacity=".22"/></filter>
    </defs>
    <path d="M-43 118 A196 196 0 0 1 208 195 L118.8 248.6 A92 92 0 0 0 1 213 Z" fill="url(#g-ask)"/>
    <path d="M211.5 201 A196 196 0 0 1 211.5 391 L120.5 340.6 A92 92 0 0 0 120.5 251.4 Z" fill="url(#g-analyse)"/>
    <path d="M208 397 A196 196 0 0 1 -43 474 L1 379 A92 92 0 0 0 118.8 343.4 Z" fill="url(#g-prior)"/>
    <circle cx="40" cy="296" r="90" fill="#fff" filter="url(#soft)"/>
    <g fill="none" stroke="#fff" stroke-width="1.6" stroke-linejoin="round">
      <path d="M100 182 h22 a3 3 0 0 1 3 3 v12 a3 3 0 0 1 -3 3 h-14 l-5 5 v-5 h-3 a3 3 0 0 1 -3 -3 v-12 a3 3 0 0 1 3 -3 z"/>
      <circle cx="130" cy="172" r="11"/>
      <path d="M106 189 h12 M106 193 h9"/>
    </g>
    <text x="130" y="176.5" font-family="Oswald,sans-serif" font-size="12" fill="#fff" text-anchor="middle">?</text>
    <g fill="none" stroke="#fff" stroke-width="1.8">
      <circle cx="172" cy="260" r="11"/>
      <path d="M164 268 l-9 10"/>
      <circle cx="184" cy="280" r="5"/>
      <circle cx="184" cy="280" r="1.6"/>
    </g>
    <g fill="#fff">
      <path d="M161 377 l6 -9 l6 9 z"/>
      <path d="M158 382 h18 l4 6 h-26 z"/>
      <path d="M152 392 h30 l4 6 h-38 z"/>
    </g>
  </svg>

  <div class="seg-text seg-text--ask">
    <h2>ASK</h2>
    <p>Our UK-wide survey of patients, carers and physiotherapists asked "What do you think are the most important unanswered questions in physiotherapy?"</p>
  </div>
  <div class="seg-text seg-text--analyse">
    <h2>ANALYSE</h2>
    <p>We reviewed 1023 questions from 388 people, and sorted these into 76 unique themed questions.</p>
  </div>
  <div class="seg-text seg-text--prioritise">
    <h2>PRIORITISE</h2>
    <p>From those we asked patients, carers, physiotherapists, nurses and surgeons to tell us "What are your top-10 most important questions". This created a shortlist that were prioritized at a final workshop.</p>
  </div>

  <div class="hub-name"><span class="hub-mark"></span>Northgate Orthopaedic Guild</div>

  <h1 class="title">
    <span class="line blue">HARRIET VOSS CONSORTIUM</span>
    <span class="line blue">PAEDIATRIC LOWER LIMB</span>
    <span class="line blue">SURGERY</span>
    <span class="line red">AGENDA FORMING</span>
    <span class="line red">COLLECTIVE</span>
  </h1>

  <div class="intro">
    <p>Surgery is often carried out amongst children with conditions that their legs, but in many conditions, it is not known which treatment works best. We need high-quality research to test which treatments are better for children.</p>
    <p>We reached out to everybody involved with children who have orthopaedic problems affecting their legs (from hip to toes), including children, parents, carers, charity workers, and all the professional groups. We asked all for their views on identifying the most important unanswered questions.</p>
  </div>

  <div class="front-partners">
    <div class="partner partner--voss"><span class="dot"></span>Harriet Voss Consortium</div>
    <div class="partner partner--kestrel"><span class="sq"></span>Kestrel Paediatric Surgical Society</div>
  </div>
</section>

<section class="page page--back">
  <h2 class="back-title">OUR TOP-10 RESEARCH PRIORITIES:</h2>

  <div class="priority priority--left" style="top:48px">
    <div class="card">What are the best ways to measure the outcome following lower limb orthopaedic surgery in children?</div>
    <div class="badge b-yellow"><span>01</span></div>
  </div>
  <div class="priority priority--right" style="top:86px">
    <div class="card">Following orthopaedic surgery to the lower limbs, what should children's rehabilitation include, how long is it expected to last and how does it affect the result of treatment?</div>
    <div class="badge b-lime"><span>02</span></div>
  </div>
  <div class="priority priority--left" style="top:125px">
    <div class="card">What is the short-term and long-term clinical and cost effectiveness of orthopaedic lower limb surgery (including best timing and technique) for children with Cerebral Palsy who can walk?</div>
    <div class="badge b-sage"><span>03</span></div>
  </div>
  <div class="priority priority--right" style="top:163px">
    <div class="card">What are the short term and long term outcomes of surgery compared to non-surgical care in the treatment of Perthes disease of the hip?</div>
    <div class="badge b-teal"><span>04</span></div>
  </div>
  <div class="priority priority--left" style="top:203px">
    <div class="card">What is the clinical and cost effectiveness of pre-operative rehabilitation in children presenting with lower limb orthopaedic conditions?</div>
    <div class="badge b-lemon"><span>05</span></div>
  </div>
  <div class="priority priority--right" style="top:241px">
    <div class="card">What is the short-term and long-term clinical and cost effectiveness of Selective Dorsal Rhizotomy (SDR) in children with Cerebral Palsy who can walk?</div>
    <div class="badge b-orange"><span>06</span></div>
  </div>
  <div class="priority priority--left" style="top:280px">
    <div class="card">Can surveillance and non-surgical treatment (e.g. physiotherapy, botulinum toxin injections, functional electrical stimulation, orthotics, casting) prevent the development of deformity requiring surgery in children with Cerebral Palsy?</div>
    <div class="badge b-teal"><span>07</span></div>
  </div>
  <div class="priority priority--right" style="top:318px">
    <div class="card">What is the best method of screening for Developmental Dysplasia of the Hip (DDH) in terms of clinical and cost effectiveness?</div>
    <div class="badge b-lemon"><span>08</span></div>
  </div>
  <div class="priority priority--left" style="top:358px">
    <div class="card">What are the best strategies to optimise communication of information between patients/carers and clinicians in order to enable shared decision-making?</div>
    <div class="badge b-sage"><span>09</span></div>
  </div>
  <div class="priority priority--right" style="top:396px">
    <div class="card">What is the best management for hip displacement in children with Cerebral Palsy?</div>
    <div class="badge b-orange"><span>10</span></div>
  </div>

  <p class="thanks">Many thanks to all those people who helped us take this work off the ground and helped us finish it!</p>

  <div class="credits">
    <h3>SPECIAL THANKS TO:</h3>
    <div class="partner partner--guild"><span class="sq"></span>Northgate Orthopaedic Guild</div>
    <div class="partner partner--kestrel"><span class="sq"></span>Kestrel Paediatric Surgical Society</div>
    <div class="partner partner--voss"><span class="dot"></span>Harriet Voss Consortium</div>
  </div>
</section>

</body>
</html>
```